1/2 Page add for BRMTL Conference

We are looking for a 1/2 page ad to support the annual BRMTL conference. I want to encourage the attendees to come to our both so we can explain how they can save money on food and supplies. here is a link to the conference. https://www.brmtl-example.org/conference/ here is our website www.pantrywisehub-example.com - the what we do can be captured in the ad. We will be at booth 505. Our goal is to get people to our booth #505 to explain the services that we provide –

Discounted food pricing
Free menu planning/design
Use of Registered Dietitian
Huge selection of discounted PPE and other necessary supplies to run any child care center

We have over 6000 members in 46 States and work with both small and large food distributors. We have been a sponsor of the association for the last 10 years.

Target Market(s)

Child care centers

Requirements
Must have
• Booth number -outline of what we do --- Stress we are a FREE service getting our members reduced pricing on food and supplies

```html
<!DOCTYPE html>
<html lang="en">
<head>
<meta charset="utf-8">
<title>PantryWise Hub – BRMTL Conference Booth 505</title>
<link rel="stylesheet" href="https://fonts.googleapis.com/css2?family=Arimo:wght@400;700&display=swap">
<style>
  :root {
    --fresh-green: #8ef06e;
    --soft-green: #c9f5b8;
    --sky-blue: #48a0f8;
    --ink: #111111;
    --white: #ffffff;
    --bowl-light: #f3eef0;
    --salad-green: #3f7a2a;
    --berry-red: #d8323f;
  }
  * { margin: 0; padding: 0; box-sizing: border-box; }
  html, body { width: 1200px; height: 733px; overflow: hidden; background: var(--white); }
  body { font-family: "Arimo", Arial, sans-serif; color: var(--ink); }
  .ad { position: relative; width: 1200px; height: 733px; overflow: hidden; background: var(--white); }

  .salad-photo {
    position: absolute; left: -91px; top: 145px; width: 536px; height: 536px; border-radius: 50%;
    background:
      radial-gradient(circle at 40% 48%, var(--berry-red) 0%, var(--salad-green) 38%, #5e8f3c 55%, var(--bowl-light) 72%, #e7e2e4 100%);
  }
  .bowl-shadow {
    position: absolute; left: 0; top: 600px; width: 420px; height: 160px; border-radius: 50%;
    background: radial-gradient(ellipse at center, #ecebeb 0%, rgba(255,255,255,0) 70%);
  }

  .brand { position: absolute; left: 79px; top: 60px; display: flex; align-items: center; gap: 8px; }
  .brand-mark { width: 20px; height: 20px; background: var(--sky-blue); }
  .brand-name { font-size: 20px; font-weight: 400; color: #5b6470; letter-spacing: -0.3px; }

  .booth-tab { position: absolute; left: 989px; top: 0; width: 138px; height: 127px; }
  .booth-label { position: absolute; left: 989px; top: 16px; width: 138px; text-align: center; color: var(--white); }
  .booth-label .word { display: block; font-size: 33px; line-height: 34px; }
  .booth-label .number { display: block; font-size: 52px; font-weight: 700; line-height: 46px; letter-spacing: -1px; }

  .headline {
    position: absolute; left: 472px; top: 78px; color: var(--fresh-green);
    font-weight: 400; font-size: 76px; line-height: 83px; letter-spacing: -0.5px; text-transform: uppercase;
  }

  .stat { position: absolute; top: 352px; width: 240px; text-align: center; }
  .stat-icon { height: 96px; display: flex; justify-content: center; align-items: flex-end; }
  .stat-text { margin-top: 14px; font-size: 17px; line-height: 22px; letter-spacing: 0.8px; }
  .stat-text strong { font-weight: 700; }
  .stat--savings-total { left: 454px; }
  .stat--reach { left: 696px; }
  .stat--rate { left: 934px; }
  .map-area {
    position: relative; width: 152px; height: 94px; border-radius: 22px 30px 40px 18px;
    background: var(--fresh-green); display: flex; align-items: center; justify-content: center;
  }
  .map-area span { color: var(--white); font-weight: 700; font-size: 21px; }

  .service-band {
    position: absolute; left: 0; top: 561px; width: 1200px; height: 141px; background: var(--sky-blue); color: var(--white);
  }
  .free-callout { position: absolute; left: 63px; top: 32px; text-transform: uppercase; }
  .free-callout .lead { display: block; font-size: 37px; font-weight: 700; line-height: 36px; }
  .free-callout .tail { display: block; font-size: 50px; font-weight: 400; line-height: 48px; letter-spacing: 0.5px; }
  .divider { position: absolute; top: 46px; width: 2px; height: 53px; background: var(--white); }
  .service-item { position: absolute; top: 38px; font-size: 25px; line-height: 34px; }
</style>
</head>
<body>
<main class="ad">
  <div class="salad-photo" role="img" aria-label="Photo of a white bowl of spinach salad with strawberries, feta, walnuts and mint"></div>
  <div class="bowl-shadow"></div>

  <div class="brand">
    <span class="brand-mark"></span>
    <span class="brand-name">PantryWise Hub</span>
  </div>

  <svg class="booth-tab" viewBox="0 0 138 127" aria-hidden="true">
    <polygon points="0,0 138,0 138,127 69,107 0,127" fill="var(--sky-blue)"/>
  </svg>
  <div class="booth-label"><span class="word">Booth</span><span class="number">505</span></div>

  <h1 class="headline">We make<br>food &amp; supply<br>purchasing easy</h1>

  <section class="stat stat--savings-total">
    <div class="stat-icon">
      <svg width="102" height="82" viewBox="0 0 102 82" aria-hidden="true">
        <polygon points="14,0 88,0 100,26 2,26" fill="var(--fresh-green)"/>
        <polygon points="20,5 82,5 90,22 12,22" fill="var(--white)"/>
        <ellipse cx="51" cy="12" rx="13" ry="9" fill="var(--fresh-green)"/>
        <text x="51" y="17" text-anchor="middle" font-size="13" font-weight="700" fill="var(--white)" font-family="Arimo, sans-serif">$</text>
        <g fill="var(--fresh-green)">
          <rect x="0" y="29" width="102" height="3"/><rect x="0" y="35" width="102" height="3"/>
          <rect x="0" y="41" width="102" height="3"/><rect x="0" y="47" width="102" height="3"/>
          <rect x="0" y="53" width="102" height="3"/><rect x="0" y="59" width="102" height="3"/>
          <rect x="0" y="65" width="102" height="3"/><rect x="0" y="71" width="102" height="3"/>
          <rect x="0" y="77" width="102" height="3"/>
        </g>
      </svg>
    </div>
    <p class="stat-text"><strong>Since 1999</strong>, we’ve saved organizations over <strong>$100,000,000</strong></p>
  </section>

  <section class="stat stat--reach">
    <div class="stat-icon">
      <div class="map-area" role="img" aria-label="Map of the United States"><span>3,000+</span></div>
    </div>
    <p class="stat-text">We serve <strong>3,000+</strong> organizations across <strong>46 states</strong></p>
  </section>

  <section class="stat stat--rate">
    <div class="stat-icon">
      <svg width="132" height="92" viewBox="0 0 132 92" aria-hidden="true">
        <path d="M30,4 L54,36 H44 V88 H16 V36 H6 Z" fill="none" stroke="var(--soft-green)" stroke-width="6" stroke-linejoin="round"/>
        <path d="M80,4 H108 V56 H120 L94,88 L68,56 H80 Z" fill="none" stroke="var(--soft-green)" stroke-width="6" stroke-linejoin="round"/>
        <circle cx="64" cy="50" r="24" fill="var(--fresh-green)"/>
        <text x="64" y="62" text-anchor="middle" font-size="34" font-weight="700" fill="var(--white)" font-family="Arimo, sans-serif">$</text>
      </svg>
    </div>
    <p class="stat-text">Estimated <strong>saving</strong> for our customers are <strong>10-35%</strong></p>
  </section>

  <section class="service-band">
    <p class="free-callout"><span class="lead">100% Free</span><span class="tail">Service</span></p>
    <span class="divider" style="left:342px"></span>
    <p class="service-item" style="left:383px">Food Menu<br>Planning/Design</p>
    <span class="divider" style="left:602px"></span>
    <p class="service-item" style="left:644px">Use of Registered<br>Dietitian</p>
    <span class="divider" style="left:880px"></span>
    <p class="service-item" style="left:922px">Discounted PPE and<br>Necessary Supplies</p>
  </section>
</main>
</body>
</html>
```